I need a business card for myself, being a proprietor of a funeral parlor based in Manila. I'd like the card to have either of the following:
White Font on Black Background
or
Black Font on White Background
No logo is needed however I will appreciate any efforts to show a symbol of eternal happiness, aptly designed with above mentioned colors in mind.
Company name, address and contact on the lower right corner.
Logo or symbol anywhere.
Quillstone Funeral Services
+639174826351
darvik4521@pelmora.com
corner of Brisco Avenue and Velhurst Street
Makati City, Philippines
Thank you.
Update: Please include a small dove in your design. You are free to choose where you would like it on the card.

```html
<!DOCTYPE html>
<html lang="en">
<head>
<meta charset="utf-8">
<title>Quillstone Funeral Services – Business Card</title>
<link rel="stylesheet" href="https://fonts.googleapis.com/css2?family=Play:wght@400&display=swap">
<style>
  :root {
    --page: #ffffff;
    --card: #000000;
    --ink: #ffffff;
    --symbol-fill: #262626;
  }
  html, body {
    margin: 0;
    padding: 0;
    width: 1200px;
    height: 1000px;
    overflow: hidden;
    background: var(--page);
  }
  .business-card {
    position: absolute;
    left: 75px;
    top: 200px;
    width: 1050px;
    height: 600px;
    background: var(--card);
    font-family: "Play", "Helvetica Neue", Arial, sans-serif;
    color: var(--ink);
  }
  .eternal-symbol {
    position: absolute;
    left: 90px;
    top: 36px;
    width: 418px;
    height: 536px;
  }
  .card-details {
    position: absolute;
    right: 82px;
    top: 22px;
    text-align: right;
  }
  .company-name {
    margin: 0;
    font-weight: 400;
    font-size: 77px;
    line-height: 91px;
    letter-spacing: 0.5px;
  }
  .contact-line {
    margin: 0;
    font-size: 33px;
    line-height: 44px;
    letter-spacing: 0.3px;
  }
  .contact-phone { margin-top: 28px; }
  .contact-email { margin-top: 15px; }
  .contact-address { margin-top: 15px; }
</style>
</head>
<body>
  <div class="business-card">
    <svg class="eternal-symbol" viewBox="0 0 418 536" role="img" aria-label="Endless knot symbol of eternal happiness in white line work">
      <polygon points="209,0 418,268 209,536 0,268" fill="var(--symbol-fill)"/>
    </svg>

    <div class="card-details">
      <h1 class="company-name">Quillstone<br>Funeral<br>Services</h1>
      <p class="contact-line contact-phone">+639174826351</p>
      <p class="contact-line contact-email">darvik4521@pelmora.com</p>
      <p class="contact-line contact-address">Corner of Brisco Avenue<br>and Velhurst Street<br>Makati City, Philippines</p>
    </div>
  </div>
</body>
</html>
```